Creative book cover for my dissertation on Crowdsourcing

I would like a book cover for my dissertation titled "Hivework: Swift Ample Nimble Study Methods for Making" author Marcus L. Fennwick. I am looking for something creative and fun. I would like it to use orange #FFA422 (CMYK 0, 36, 87, 0) and or blue #00A6D6 (CMYK 100, 22, 0, 16). The cover will be printed in full color and you are welcome to use other colors, images or drawn graphics. Included is a image I purchased on PixVault a few years back. For reference I have also attached a graphic used in the paper - there are several graphics of this style in the paper. I look forward to seeing your incredible design.

Target Market(s)

Industrial Designers, Designers, Students, Researchers

Requirements
Must have
• Title and author name

```html
<!DOCTYPE html>
<html lang="en">
<head>
<meta charset="utf-8">
<title>Hivework — Book Cover</title>
<link rel="stylesheet" href="https://fonts.googleapis.com/css2?family=Oswald:wght@600;700&family=Cinzel:wght@600&display=swap">
<style>
  :root {
    --paper: #ffffff;
    --orange-deep: #f7861c;
    --orange-bright: #ffa422;
    --crowd-tone: #9d918d;
    --crowd-soft: #e4e0de;
    --author-ink: #3a3a3a;
  }
  * { margin: 0; padding: 0; box-sizing: border-box; }
  html, body {
    width: 800px;
    height: 1200px;
    overflow: hidden;
    background: var(--paper);
  }
  .cover {
    position: relative;
    width: 800px;
    height: 1200px;
    background: var(--paper);
    text-align: center;
  }
  .title-block {
    position: absolute;
    top: 92px;
    left: 0;
    width: 100%;
    font-family: "Oswald", "Arial Narrow", sans-serif;
    text-transform: uppercase;
  }
  .title {
    font-weight: 700;
    font-size: 132px;
    line-height: 1;
    letter-spacing: 6px;
    background: linear-gradient(180deg, var(--orange-deep) 0%, var(--orange-bright) 100%);
    -webkit-background-clip: text;
    background-clip: text;
    color: transparent;
  }
  .subtitle {
    margin-top: 14px;
    font-weight: 600;
    font-size: 46px;
    line-height: 1;
    letter-spacing: 0.5px;
    color: var(--orange-deep);
  }
  .subtitle-tail {
    margin-top: 18px;
    font-weight: 600;
    font-size: 54px;
    line-height: 1;
    letter-spacing: 1px;
    color: var(--orange-deep);
  }
  .crowd-photo {
    position: absolute;
    top: 410px;
    left: 50px;
    width: 700px;
    height: 500px;
    background: radial-gradient(ellipse 50% 42% at 50% 52%, var(--crowd-tone) 0%, var(--crowd-soft) 60%, var(--paper) 100%);
  }
  .author {
    position: absolute;
    top: 1062px;
    left: 0;
    width: 100%;
    font-family: "Cinzel", "Times New Roman", serif;
    font-weight: 600;
    font-size: 40px;
    line-height: 1;
    letter-spacing: 2px;
    color: var(--author-ink);
  }
</style>
</head>
<body>
  <main class="cover">
    <header class="title-block">
      <h1 class="title">Hivework</h1>
      <p class="subtitle">Swift Ample Nimble Study Methods</p>
      <p class="subtitle-tail">For Making</p>
    </header>
    <div class="crowd-photo" role="img" aria-label="Aerial photograph of a large crowd of people standing together to form the shape of an eye on a white ground"></div>
    <p class="author">Marcus L. Fennwick</p>
  </main>
</body>
</html>
```